Meridian Rest Supply Needs Business Card

Looking for a very nice looking business card. Creative but not extravagant. We sell beds and pillows across the U.S. and need something professional but catchy. I have attached the logo.

Name : Dale Fenwick
Title : President
Phone : (800) 417-2964
Email: sleep@quorvana.com
Website: www.quorvana.com

Can be single-sided or double-sided
horizontal or vertical

Can use Blues/Greys

Target Market(s)

Mass Market

Industry/Entity Type

Retail

Contact Information for Business Card

Name : Dale Fenwick
Title : President
Phone : (800) 417-2964
Email: sleep@quorvana.com
Website: www.quorvana.com

Requirements
Must have
• Clean, Modern, Smooth
• Can use Blues/Greys
• On the other side without the information - have something simple like www.quorvana.com or our logo
Nice to have
• Surprise me
Should not have
• Nothing crazy, nothing cluttered

```html
<!DOCTYPE html>
<html lang="en">
<head>
<meta charset="utf-8">
<title>Quorvana Business Card</title>
<link rel="stylesheet" href="https://fonts.googleapis.com/css2?family=Open+Sans:wght@300;400;700&display=swap">
<style>
  :root {
    --stage: #2e2f33;
    --card-grey: #505052;
    --brand-blue: #38bfea;
    --ink: #1d2a33;
    --white: #ffffff;
  }
  * { margin: 0; padding: 0; box-sizing: border-box; }
  html, body { width: 1200px; height: 1200px; overflow: hidden; }
  body {
    background: var(--stage);
    font-family: "Open Sans", sans-serif;
    position: relative;
  }
  .card {
    position: absolute;
    left: 250px;
    width: 700px;
    height: 400px;
    overflow: hidden;
    box-shadow: 0 10px 30px rgba(0,0,0,0.35);
  }
  .wordmark { white-space: nowrap; font-weight: 300; line-height: 1; }
  /* Back side */
  .card-back { top: 150px; background: var(--card-grey); }
  .card-back .wordmark {
    position: absolute;
    left: 140px;
    top: 125px;
    font-size: 104px;
    letter-spacing: 1px;
    color: var(--brand-blue);
  }
  .card-back .base-band {
    position: absolute;
    left: 0; bottom: 0;
    width: 700px; height: 60px;
  }
  .card-back .tab-url {
    position: absolute;
    left: 150px;
    bottom: 14px;
    width: 230px;
    text-align: center;
    font-size: 14px;
    letter-spacing: 4px;
    white-space: nowrap;
    color: var(--white);
  }
  /* Front side */
  .card-front { top: 650px; background: var(--brand-blue); }
  .contact-block {
    position: absolute;
    left: 50px;
    top: 105px;
    color: var(--ink);
  }
  .contact-block .person-name {
    font-weight: 700;
    font-size: 20px;
    text-transform: uppercase;
    letter-spacing: 0.3px;
  }
  .contact-block .person-title {
    font-size: 18px;
    margin-bottom: 18px;
  }
  .contact-list { list-style: none; font-size: 15px; line-height: 1.75; }
  .contact-list li { display: flex; align-items: center; gap: 8px; white-space: nowrap; }
  .contact-list svg { width: 13px; height: 13px; flex: none; }
  .divider {
    position: absolute;
    left: 300px;
    top: 85px;
    width: 2px;
    height: 230px;
    background: var(--white);
  }
  .card-front .wordmark {
    position: absolute;
    left: 340px;
    top: 160px;
    font-size: 66px;
    letter-spacing: 1px;
    color: var(--white);
  }
</style>
</head>
<body>

  <section class="card card-back" aria-label="Card back">
    <div class="wordmark">quorvana</div>
    <svg class="base-band" viewBox="0 0 700 60" aria-hidden="true">
      <path fill="#38bfea" d="M0 46 H135 Q148 46 150 36 Q152 22 168 22 H362 Q378 22 380 36 Q382 46 395 46 H700 V60 H0 Z"/>
    </svg>
    <div class="tab-url">www.quorvana.com</div>
  </section>

  <section class="card card-front" aria-label="Card front">
    <div class="contact-block">
      <div class="person-name">Dale Fenwick</div>
      <div class="person-title">President</div>
      <ul class="contact-list">
        <li>
          <svg viewBox="0 0 24 24" aria-hidden="true"><path fill="#1d2a33" d="M6.6 10.8a15.1 15.1 0 0 0 6.6 6.6l2.2-2.2a1 1 0 0 1 1-.25 11.4 11.4 0 0 0 3.6.57 1 1 0 0 1 1 1V20a1 1 0 0 1-1 1A17 17 0 0 1 3 4a1 1 0 0 1 1-1h3.5a1 1 0 0 1 1 1c0 1.25.2 2.450.57 3.57a1 1 0 0 1-.25 1z"/></svg>
          (800) 417-2964
        </li>
        <li>
          <svg viewBox="0 0 24 24" aria-hidden="true"><path fill="#1d2a33" d="M2 5h20v14H2z M2 5l10 8 10-8" stroke="#38bfea" stroke-width="1.5"/></svg>
          sleep@quorvana.com
        </li>
        <li>
          <svg viewBox="0 0 24 24" aria-hidden="true"><g fill="none" stroke="#1d2a33" stroke-width="2"><circle cx="12" cy="12" r="10"/><path d="M2 12h20M12 2c3 3 3 17 0 20M12 2c-3 3-3 17 0 20"/></g></svg>
          www.quorvana.com
        </li>
      </ul>
    </div>
    <div class="divider"></div>
    <div class="wordmark">quorvana</div>
  </section>

</body>
</html>
```